One of a Kind Clean Business Card

We need to design a new business card template for our company. Our company designs and produced merchandising displays. You can see a sample of what we produce on our site www.qorvatrim.com. I have uploaded our logo in vector format, as well as a picture of our current business cards. We want a totally different look. We want simple and clean, looking forward to seeing what people create.
Updates

I would like to update the address for Teblo Display Group Inc. 418 N Harlow Ln Arlington Heights, IL 60117 Would also note. No QR codes

Industry/Entity Type

Business

Contact Information for Business Card

Need a 1 sided business card designed.

Font styles to use
Serif

Requirements
Must have
• Easy to view; Clean Design
Nice to have
• Features that promote engineering and creativity
Should not have
• Too much clutter, keep it simple

```html
<!DOCTYPE html>
<html lang="en">
<head>
<meta charset="utf-8">
<title>Teblo Display Group Inc. – Business Cards</title>
<link href="https://fonts.googleapis.com/css2?family=Open+Sans:wght@400&family=Roboto:wght@400;500&display=swap" rel="stylesheet">
<style>
  :root {
    --page-bg: #ece9e4;
    --card-bg: #ffffff;
    --ink: #1d1d1d;
    --ink-soft: #3e3e3e;
    --brand-red: #8e1a1a;
    --card-shadow: rgba(0, 0, 0, 0.18);
  }
  * { margin: 0; padding: 0; box-sizing: border-box; }
  html, body {
    width: 1200px;
    height: 1200px;
    overflow: hidden;
    background: var(--page-bg);
  }
  .sheet {
    position: relative;
    width: 1200px;
    height: 1200px;
  }
  .card {
    position: absolute;
    left: 210px;
    width: 780px;
    height: 440px;
    background: var(--card-bg);
    box-shadow: 0 6px 18px var(--card-shadow);
    overflow: hidden;
    font-family: "Open Sans", sans-serif;
    color: var(--ink-soft);
  }
  .card--shelf { top: 150px; }
  .card--tray { top: 630px; }

  .brand {
    position: absolute;
    left: 45px;
    top: 96px;
    display: flex;
    align-items: center;
    gap: 12px;
  }
  .brand-mark {
    width: 14px;
    height: 14px;
    background: var(--brand-red);
  }
  .brand-name {
    font-family: "Roboto", sans-serif;
    font-weight: 400;
    font-size: 28px;
    color: var(--brand-red);
    letter-spacing: 0.2px;
  }

  .person {
    position: absolute;
    right: 45px;
    top: 50px;
    text-align: right;
    font-family: "Roboto", sans-serif;
  }
  .person-name {
    font-weight: 500;
    font-size: 30px;
    color: var(--ink);
    line-height: 1.1;
  }
  .person-title {
    font-weight: 400;
    font-size: 19px;
    color: var(--brand-red);
    margin-top: 3px;
  }

  .address {
    position: absolute;
    left: 45px;
    top: 232px;
    font-size: 17.5px;
    line-height: 26px;
  }
  .contacts {
    position: absolute;
    left: 45px;
    top: 300px;
    list-style: none;
    font-size: 17.5px;
    line-height: 28px;
  }
  .contacts li {
    display: flex;
    align-items: center;
    gap: 8px;
  }
  .contacts svg {
    width: 17px;
    height: 17px;
    flex: none;
  }

  .product-photo {
    position: absolute;
  }
  .card--shelf .product-photo {
    left: 495px;
    top: 185px;
    width: 250px;
    height: 245px;
    background: linear-gradient(160deg, #b9865a 0%, #7c4a2c 45%, #2b2b2b 100%);
    border-radius: 4px;
  }
  .card--tray .product-photo {
    left: 445px;
    top: 200px;
    width: 335px;
    height: 240px;
    background: linear-gradient(150deg, #5a5a5a 0%, #222222 60%, #e6e6e6 100%);
  }
</style>
</head>
<body>
<main class="sheet">

  <section class="card card--shelf">
    <div class="brand"><span class="brand-mark"></span><span class="brand-name">Teblo Display Group Inc.</span></div>
    <div class="person">
      <div class="person-name">DANE HOLLICK</div>
      <div class="person-title">President &amp; CEO</div>
    </div>
    <p class="address">418 N Harlow Ln<br>Arlington Heights, IL 60117</p>
    <ul class="contacts">
      <li><svg viewBox="0 0 16 16"><path d="M3 1.5l3 .5 1 3.2-1.8 1.3a8 8 0 0 0 4.3 4.3L10.8 9l3.2 1 .5 3-1.8 1.6C7.5 14.5 1.5 8.5 1.4 3.3z" fill="none" stroke="var(--brand-red)" stroke-width="1.3"/></svg>815-555-0142</li>
      <li><svg viewBox="0 0 16 16"><rect x="4" y="1" width="8" height="14" rx="1.5" fill="none" stroke="var(--brand-red)" stroke-width="1.3"/><line x1="7" y1="12.5" x2="9" y2="12.5" stroke="var(--brand-red)" stroke-width="1.3"/></svg>312-555-0176</li>
      <li><svg viewBox="0 0 16 16"><rect x="1" y="3.5" width="14" height="9" fill="none" stroke="var(--brand-red)" stroke-width="1.3"/><path d="M1 3.5l7 5 7-5" fill="none" stroke="var(--brand-red)" stroke-width="1.3"/></svg>dhollick@qorvatrim.com</li>
      <li><svg viewBox="0 0 16 16"><circle cx="8" cy="8" r="6.5" fill="var(--brand-red)"/><path d="M1.5 8h13M8 1.5c-2.5 3-2.5 10 0 13M8 1.5c2.5 3 2.5 10 0 13" fill="none" stroke="#fff" stroke-width="1"/></svg>www.qorvatrim.com</li>
    </ul>
    <div class="product-photo" role="img" aria-label="Photo of a two-tier black merchandising rack stocked with coffee bags"></div>
  </section>

  <section class="card card--tray">
    <div class="brand"><span class="brand-mark"></span><span class="brand-name">Teblo Display Group Inc.</span></div>
    <div class="person">
      <div class="person-name">DANE HOLLICK</div>
      <div class="person-title">President &amp; CEO</div>
    </div>
    <p class="address">418 N Harlow Ln<br>Arlington Heights, IL 60117</p>
    <ul class="contacts">
      <li><svg viewBox="0 0 16 16"><path d="M3 1.5l3 .5 1 3.2-1.8 1.3a8 8 0 0 0 4.3 4.3L10.8 9l3.2 1 .5 3-1.8 1.6C7.5 14.5 1.5 8.5 1.4 3.3z" fill="none" stroke="var(--brand-red)" stroke-width="1.3"/></svg>815-555-0142</li>
      <li><svg viewBox="0 0 16 16"><rect x="4" y="1" width="8" height="14" rx="1.5" fill="none" stroke="var(--brand-red)" stroke-width="1.3"/><line x1="7" y1="12.5" x2="9" y2="12.5" stroke="var(--brand-red)" stroke-width="1.3"/></svg>312-555-0176</li>
      <li><svg viewBox="0 0 16 16"><rect x="1" y="3.5" width="14" height="9" fill="none" stroke="var(--brand-red)" stroke-width="1.3"/><path d="M1 3.5l7 5 7-5" fill="none" stroke="var(--brand-red)" stroke-width="1.3"/></svg>dhollick@qorvatrim.com</li>
      <li><svg viewBox="0 0 16 16"><circle cx="8" cy="8" r="6.5" fill="var(--brand-red)"/><path d="M1.5 8h13M8 1.5c-2.5 3-2.5 10 0 13M8 1.5c2.5 3 2.5 10 0 13" fill="none" stroke="#fff" stroke-width="1"/></svg>www.qorvatrim.com</li>
    </ul>
    <div class="product-photo" role="img" aria-label="Close-up photo of a black plastic shelf tray with a spring pusher divider"></div>
  </section>

</main>
</body>
</html>
```